Social Media Infographic for White Paper

Am working on a white paper on social media use by C-Suite Executives, and hope to include some infographics. I would like some help designing the first infographic.

The master bit of information is that "66% of C-Suite Executives use social media for professional purpose."

Within that 66%
-70% post original content on a daily/weekly basis
-13% of professional users are lurkers
-40% plan to use social media even more in the future

After initial design will need to two versions of the infographic, one listing the source at the bottom in small print (Source: 2017 Tollery Partners Executive Social Media Study), the other one with no source information.

Infographic design should be complimentary with my website: www.tollerypartners.example, but use of green should be very limited, if at all.

Target Market(s)

New media, C-Suite Executives, Executive Coaches

Industry/Entity Type

Management Consulting

Font styles to use
Sans Serif

Requirements
Must have
• Infographic with data displayed in a easy to understand format that tells the story of C-Suite Executives that participate in social media for professional purposes.
Nice to have
• Complements website design - www.tollery.example.
Should not have
• Limit use of green from website logo, which can be overpowering. Some is ok, but not too much

```html
<!DOCTYPE html>
<html lang="en">
<head>
<meta charset="utf-8">
<title>C-Suite Executives on Social Media</title>
<link href="https://fonts.googleapis.com/css2?family=Raleway:wght@300;400&family=Roboto+Condensed:wght@300&family=Open+Sans:wght@400&display=swap" rel="stylesheet">
<style>
  :root {
    --ink: #555759;
    --ink-soft: #5f6163;
    --teal: #7fe3cb;
    --ring-green: #3ddc9a;
    --ring-grey: #cfcfcf;
    --dot: #2fd99a;
    --line: #b3b3b3;
    --bar-daily: #1b6a45;
    --bar-future: #abf6d9;
    --bar-lurk: #5ff3f1;
    --icon-calendar: #1d2e42;
    --icon-search: #4a4a4a;
    --suit: #121616;
    --bg: #ffffff;
  }
  html, body {
    margin: 0;
    padding: 0;
    width: 1200px;
    height: 971px;
    overflow: hidden;
    background: var(--bg);
  }
  .infographic {
    position: relative;
    width: 1200px;
    height: 971px;
    font-family: "Open Sans", sans-serif;
    color: var(--ink);
  }
  .lines {
    position: absolute;
    left: 0;
    top: 0;
  }
  .headline {
    position: absolute;
    left: 377px;
    top: 78px;
    margin: 0;
    font-family: "Raleway", sans-serif;
    font-weight: 400;
    font-size: 30px;
    line-height: 38px;
    letter-spacing: 0.5px;
    color: var(--ink);
    text-transform: uppercase;
  }
  .headline .accent { color: var(--teal); }
  .hero-figure {
    position: absolute;
    left: 0;
    top: 62px;
    width: 268px;
    text-align: center;
    font-family: "Roboto Condensed", sans-serif;
    font-weight: 300;
    font-size: 104px;
    line-height: 1;
    letter-spacing: -3px;
    color: var(--ink);
  }
  .stat-value {
    position: absolute;
    right: 386px;
    font-family: "Roboto Condensed", sans-serif;
    font-weight: 300;
    font-size: 96px;
    line-height: 1;
    letter-spacing: -3px;
    color: var(--ink);
  }
  .stat-value--daily { top: 356px; }
  .stat-value--future { top: 542px; }
  .stat-value--lurk { top: 744px; }
  .stat-caption {
    position: absolute;
    right: 392px;
    margin: 0;
    text-align: right;
    font-size: 18px;
    line-height: 27px;
    color: var(--ink-soft);
  }
  .stat-caption--daily { top: 455px; }
  .stat-caption--future { top: 642px; }
  .stat-caption--lurk { top: 843px; }
  .bar { position: absolute; height: 12px; }
  .bar--daily { left: 88px; top: 430px; width: 543px; background: var(--bar-daily); }
  .bar--future { left: 271px; top: 611px; width: 363px; background: var(--bar-future); }
  .bar--lurk { left: 522px; top: 815px; width: 109px; background: var(--bar-lurk); }
  .networks {
    position: absolute;
    left: 266px;
    top: 555px;
    display: flex;
    gap: 18px;
    font-size: 16px;
    line-height: 22px;
    color: var(--ink-soft);
  }
  .network { display: flex; align-items: center; gap: 6px; }
  .network::before {
    content: "";
    width: 12px;
    height: 12px;
    border-radius: 50%;
    background: var(--ink-soft);
  }
  .executive {
    position: absolute;
    left: 876px;
    top: 86px;
    width: 318px;
    height: 852px;
    border-radius: 120px 120px 20px 20px;
    background: linear-gradient(180deg, #2e3535 0%, var(--suit) 22%, var(--suit) 100%);
  }
</style>
</head>
<body>
<main class="infographic">

  <svg class="lines" width="1200" height="971" viewBox="0 0 1200 971" aria-hidden="true">
    <path d="M134 7 A127 127 0 0 1 241.2 202" fill="none" stroke="var(--ring-grey)" stroke-width="14"/>
    <path d="M134 7 A127 127 0 1 0 241.2 202" fill="none" stroke="var(--ring-green)" stroke-width="14"/>

    <g fill="none" stroke="var(--line)" stroke-width="3" stroke-dasharray="2 5">
      <polyline points="268,134 327,134 327,219 807,219 807,342"/>
      <polyline points="807,900 807,962 1188,962"/>
    </g>
    <circle cx="808" cy="219" r="7" fill="var(--dot)"/>
    <circle cx="1189" cy="962" r="7" fill="var(--dot)"/>

    <g class="icon-calendar" fill="none" stroke="var(--icon-calendar)" stroke-width="6" stroke-linejoin="round" stroke-linecap="round">
      <rect x="98" y="334" width="88" height="76" rx="6"/>
      <line x1="98" y1="358" x2="186" y2="358"/>
      <line x1="118" y1="322" x2="118" y2="340"/>
      <line x1="166" y1="322" x2="166" y2="340"/>
    </g>

    <g class="icon-search" fill="none" stroke="var(--icon-search)" stroke-linecap="round">
      <circle cx="432" cy="758" r="30" stroke-width="6"/>
      <line x1="455" y1="781" x2="496" y2="822" stroke-width="7"/>
    </g>
  </svg>

  <div class="hero-figure">66%</div>
  <h1 class="headline">Of <span class="accent">C-Suite Executives</span><br>use social media for<br>professional purposes</h1>

  <div class="bar bar--daily"></div>
  <div class="stat-value stat-value--daily">70%</div>
  <p class="stat-caption stat-caption--daily">post original content on a daily/weekly basis</p>

  <div class="networks">
    <span class="network">Postwell</span>
    <span class="network">Clipline</span>
    <span class="network">Murmur</span>
  </div>
  <div class="bar bar--future"></div>
  <div class="stat-value stat-value--future">40%</div>
  <p class="stat-caption stat-caption--future">plan to use social media even more<br>in the future</p>

  <div class="bar bar--lurk"></div>
  <div class="stat-value stat-value--lurk">13%</div>
  <p class="stat-caption stat-caption--lurk">of professional users are lurkers</p>

  <div class="executive" role="img" aria-label="Illustration of a businessman in a dark suit and green tie looking at his smartphone"></div>

</main>
</body>
</html>
```